The Quiet Lantern - Your trusted map at hand

The Quiet Lantern (فانوس آرام in Persian)

We need a new app design for a major update on Android, iOS and Windows Universal platforms.
Our company works on creating innovative apps and games on different platforms, this particular app is free for end users and provides location based services. Here is the abstract feature list:
• Nearest points around user (explore on map or find) including locations, events and skills
• Add points to our database (partners) plus comments and ratings
• Point owners can modify or complete their points data, provide sale events, services and …

Attachments:
Our service logo
The detailed descriptions of different sections (PDF documents)
Updates

Project Deadline Extended Reason: We want more designs :)Give us previews on Home and Map sections at least (more interesting if previews are provided for more sections) Added Saturday, January 7, 2017

Target Market(s)

Public

Industry/Entity Type

Android

Font styles to use
Serif
Sans Serif

Requirements
Must have
• Consider attached service logo & wireframe
• Designs for attached sections
• Fluent user experience
• Modern design
Nice to have
• Right to Left layouts
Should not have
• No alphabet in graphic assets

```html
<!DOCTYPE html>
<html lang="en">
<head>
<meta charset="utf-8">
<title>The Quiet Lantern – Home</title>
<link href="https://fonts.googleapis.com/css2?family=Quicksand:wght@400;500;600&display=swap" rel="stylesheet">
<style>
  :root{
    --bg:#1d8fd5;
    --screen:#ffffff;
    --brand-blue:#1a6fe0;
    --text:#2b2b2b;
    --muted:#8a8a8a;
    --star:#f7b924;
    --map-light:#ece8e0;
    --map-mid:#d9d4c8;
    --map-green:#cfe3b8;
    --map-water:#aec9f0;
    --pin-yellow:#f9c532;
    --pin-teal:#4fd6b4;
    --pin-cyan:#4fd2f0;
    --pin-purple:#b27ce8;
  }
  *{box-sizing:border-box;margin:0;padding:0}
  html,body{width:1200px;height:864px;overflow:hidden}
  body{background:var(--bg);font-family:"Quicksand",sans-serif;color:var(--text);position:relative}

  .app-screen{position:absolute;left:370px;top:22px;width:460px;height:820px;background:var(--screen);overflow:hidden;box-shadow:0 20px 50px rgba(0,0,0,.25)}

  .status-bar{height:24px;display:flex;align-items:center;justify-content:space-between;padding:0 10px;font-size:12px;color:var(--brand-blue);font-weight:500}
  .status-bar .carrier{display:flex;align-items:center;gap:4px}
  .status-bar .signal{display:flex;gap:2px}
  .status-bar .signal i{width:6px;height:6px;border-radius:50%;background:var(--brand-blue)}
  .status-bar .signal i.off{background:none;border:1px solid var(--brand-blue)}
  .status-bar .battery{display:flex;align-items:center;gap:4px}
  .status-bar .battery-cell{width:22px;height:10px;border:1px solid var(--brand-blue);border-radius:2px;padding:1px}
  .status-bar .battery-cell span{display:block;width:77%;height:100%;background:var(--brand-blue)}

  .app-header{height:52px;display:flex;align-items:center;justify-content:space-between;padding:0 16px}
  .app-header h1{font-size:22px;font-weight:500;color:var(--brand-blue);letter-spacing:1px}
  .menu-icon,.search-icon{width:26px;height:26px}

  .map-area{position:absolute;top:76px;left:0;right:0;bottom:0;background:
    radial-gradient(ellipse at 88% 40%,var(--map-water) 0 18%,transparent 19%),
    radial-gradient(ellipse at 30% 60%,var(--map-green) 0 6%,transparent 7%),
    linear-gradient(160deg,var(--map-light),var(--map-mid))}

  .map-pin{position:absolute;width:46px;height:40px;border-radius:10px;display:flex;align-items:center;justify-content:center;box-shadow:0 4px 8px rgba(0,0,0,.18)}
  .map-pin svg{width:22px;height:22px}
  .pin-yellow{background:var(--pin-yellow)}
  .pin-teal{background:var(--pin-teal)}
  .pin-cyan{background:var(--pin-cyan)}
  .pin-purple{background:var(--pin-purple)}

  .suggestion-strip{position:absolute;left:0;right:0;top:540px;height:200px}
  .place-card{position:absolute;top:0;height:180px;background:#fff;border-radius:8px;box-shadow:0 8px 22px rgba(0,0,0,.18);padding:22px}
  .place-card.left{left:-150px;width:250px;text-align:right;padding-right:16px}
  .place-card.center{left:115px;width:230px}
  .place-card.right{left:360px;width:250px;padding-left:16px}
  .place-card .category{width:44px;height:36px;border-radius:8px;background:var(--pin-teal);display:flex;align-items:center;justify-content:center;margin-bottom:14px}
  .place-card .category svg{width:22px;height:22px}
  .place-card h2{font-size:19px;font-weight:500;line-height:1.25}
  .place-card.left h2{margin-top:60px}
  .place-card .distance{font-size:13px;color:var(--muted);margin-top:6px}
  .place-card .rating{position:absolute;right:20px;bottom:18px;color:var(--star);font-size:22px;display:flex;align-items:center;gap:6px}
  .place-card.left .rating{right:16px}
  .place-card .rating svg{width:16px;height:16px}

  .more-link{position:absolute;left:0;right:0;top:765px;text-align:center;font-size:18px;font-weight:500;color:var(--brand-blue)}
</style>
</head>
<body>
<main class="app-screen">
  <div class="status-bar">
    <div class="carrier"><span class="signal"><i></i><i></i><i></i><i class="off"></i><i class="off"></i></span>Nimbus</div>
    <div class="time">1:23 AM</div>
    <div class="battery">77%<span class="battery-cell"><span></span></span></div>
  </div>

  <header class="app-header">
    <svg class="menu-icon" viewBox="0 0 26 26" fill="none" stroke="#1a6fe0" stroke-width="2"><path d="M3 7h20M3 13h20M3 19h20"/></svg>
    <h1>HOME</h1>
    <svg class="search-icon" viewBox="0 0 26 26" fill="none" stroke="#1a6fe0" stroke-width="2.5"><circle cx="11" cy="11" r="7"/><path d="M16 16l7 7"/></svg>
  </header>

  <section class="map-area" role="img" aria-label="Street map of the city centre with nearby points">
    <div class="map-pin pin-yellow" style="left:120px;top:40px"><svg viewBox="0 0 24 24" fill="none" stroke="#fff" stroke-width="1.5"><circle cx="9" cy="12" r="5"/><circle cx="15" cy="12" r="5"/></svg></div>
    <div class="map-pin pin-cyan" style="left:300px;top:30px"><svg viewBox="0 0 24 24" fill="none" stroke="#fff" stroke-width="1.5"><path d="M3 20L12 5l9 15z M12 20v-6"/></svg></div>
    <div class="map-pin pin-purple" style="left:190px;top:110px"><svg viewBox="0 0 24 24" fill="none" stroke="#fff" stroke-width="1.5"><path d="M6 21V4h11l-2 4 2 4H6"/></svg></div>
    <div class="map-pin pin-purple" style="left:330px;top:170px"><svg viewBox="0 0 24 24" fill="none" stroke="#fff" stroke-width="1.5"><path d="M3 20L12 5l9 15z M12 20v-6"/></svg></div>
    <div class="map-pin pin-cyan" style="left:60px;top:200px"><svg viewBox="0 0 24 24" fill="none" stroke="#fff" stroke-width="1.5"><circle cx="9" cy="12" r="5"/><circle cx="15" cy="12" r="5"/></svg></div>
    <div class="map-pin pin-teal" style="left:200px;top:190px"><svg viewBox="0 0 24 24" fill="none" stroke="#fff" stroke-width="1.5"><circle cx="9" cy="12" r="5"/><circle cx="15" cy="12" r="5"/></svg></div>
    <div class="map-pin pin-yellow" style="left:240px;top:250px"><svg viewBox="0 0 24 24" fill="none" stroke="#fff" stroke-width="1.5"><path d="M3 20L12 5l9 15z M12 20v-6"/></svg></div>
    <div class="map-pin pin-teal" style="left:150px;top:310px"><svg viewBox="0 0 24 24" fill="none" stroke="#fff" stroke-width="1.5"><path d="M6 21V4h11l-2 4 2 4H6"/></svg></div>
    <div class="map-pin pin-yellow" style="left:30px;top:360px"><svg viewBox="0 0 24 24" fill="none" stroke="#fff" stroke-width="1.5"><path d="M3 20L12 5l9 15z M12 20v-6"/></svg></div>
    <div class="map-pin pin-yellow" style="left:370px;top:330px"><svg viewBox="0 0 24 24" fill="none" stroke="#fff" stroke-width="1.5"><circle cx="9" cy="12" r="5"/><circle cx="15" cy="12" r="5"/></svg></div>
  </section>

  <section class="suggestion-strip">
    <article class="place-card left">
      <h2>Hotel</h2>
      <div class="rating"><svg viewBox="0 0 24 24" fill="#f7b924"><path d="M12 2l3 7h7l-6 5 2 8-6-4-6 4 2-8-6-5h7z"/></svg>3.9</div>
    </article>
    <article class="place-card center">
      <div class="category"><svg viewBox="0 0 24 24" fill="none" stroke="#fff" stroke-width="1.5"><path d="M6 21V4h11l-2 4 2 4H6"/></svg></div>
      <h2>Ridge Walkers<br>Club</h2>
      <p class="distance">2.2 miles</p>
      <div class="rating"><svg viewBox="0 0 24 24" fill="#f7b924"><path d="M12 2l3 7h7l-6 5 2 8-6-4-6 4 2-8-6-5h7z"/></svg>4.2</div>
    </article>
    <article class="place-card right">
      <div class="category"><svg viewBox="0 0 24 24" fill="none" stroke="#fff" stroke-width="1.5"><path d="M6 21V4h11l-2 4 2 4H6"/></svg></div>
      <h2>Fernhall<br>Arena</h2>
      <p class="distance">7.4 miles</p>
    </article>
  </section>

  <a class="more-link">More Suggestions</a>
</main>
</body>
</html>
```